Timber Ridge Land Services Business Cards

Need to create a business card with the company logo "Timber Ridge Land Services". The business will provide forestry mulching for land clearing and vegetation control, brush and small tree removal, wildlife habitat improvement and trail and property access creation.

```html
<!DOCTYPE html>
<html lang="en">
<head>
<meta charset="utf-8">
<title>Timber Ridge Land Services – Business Cards</title>
<link href="https://fonts.googleapis.com/css2?family=Poppins:wght@300;400;500;700&display=swap" rel="stylesheet">
<style>
  :root {
    --backdrop: #262626;
    --forest: #0e5c4c;
    --forest-deep: #0a4a3c;
    --leaf: #6cc070;
    --leaf-pale: #a9dc8f;
    --paper: #ffffff;
  }
  * { margin: 0; padding: 0; box-sizing: border-box; }
  html, body { width: 1200px; height: 711px; overflow: hidden; }
  body {
    background: var(--backdrop);
    font-family: "Poppins", sans-serif;
    position: relative;
  }
  .card {
    position: absolute;
    top: 76px;
    width: 320px;
    height: 560px;
    border-radius: 26px;
    overflow: hidden;
    box-shadow: 0 18px 40px rgba(0,0,0,.55);
  }

  /* Back card */
  .card-back { left: 250px; background: var(--forest); }
  .back-pattern {
    position: absolute; inset: 0;
    background: linear-gradient(135deg, var(--leaf-pale) 0%, #2f9a52 22%, var(--forest) 55%, var(--forest-deep) 100%);
  }
  .back-wordmark {
    position: absolute;
    left: 50%; top: 50%;
    transform: translate(-50%, -50%) rotate(-90deg);
    display: flex; align-items: center; gap: 14px;
    white-space: nowrap;
    color: var(--paper);
    font-weight: 700;
    font-size: 26px;
    letter-spacing: .5px;
  }
  .back-wordmark .mark-square { width: 22px; height: 22px; background: var(--paper); }

  /* Front card */
  .card-front { left: 630px; background: var(--forest); }
  .front-top {
    position: absolute; inset: 0 0 auto 0; height: 250px;
    background: var(--paper);
  }
  .front-curve { position: absolute; left: 0; top: 190px; width: 320px; height: 90px; }
  .front-wordmark {
    position: absolute; top: 82px; left: 0; right: 0;
    display: flex; flex-direction: column; align-items: center; gap: 10px;
    color: var(--forest);
    font-weight: 700; font-size: 19px; text-align: center; line-height: 1.2;
  }
  .front-wordmark .mark-square { width: 18px; height: 18px; background: var(--forest); }

  .person { position: absolute; top: 300px; left: 0; right: 0; text-align: center; color: var(--paper); }
  .person-name { font-size: 27px; line-height: 1.1; color: var(--leaf); }
  .person-name .first { font-weight: 700; }
  .person-name .last { font-weight: 300; }
  .person-role { font-size: 13px; font-weight: 500; margin-top: 2px; }

  .divider {
    position: absolute; left: 34px; right: 34px;
    display: flex; align-items: center; justify-content: center; gap: 8px;
  }
  .divider::before, .divider::after { content: ""; flex: 1; height: 1px; background: var(--leaf); }
  .icon { width: 20px; height: 20px; }
  .divider-contact { top: 370px; }
  .divider-address { top: 462px; }

  .contact-list {
    position: absolute; top: 400px; left: 0; right: 0;
    list-style: none; text-align: center;
    color: var(--paper); font-size: 13px; font-weight: 500; line-height: 1.5;
  }
  .address {
    position: absolute; top: 494px; left: 0; right: 0;
    text-align: center; font-style: normal;
    color: var(--paper); font-size: 13px; font-weight: 500; line-height: 1.5;
  }
</style>
</head>
<body>

<section class="card card-back" aria-label="Card back">
  <div class="back-pattern" role="img" aria-label="Repeating decorative brand pattern in green tones"></div>
  <div class="back-wordmark"><span class="mark-square"></span>Timber Ridge Land Services</div>
</section>

<section class="card card-front" aria-label="Card front">
  <div class="front-top"></div>
  <svg class="front-curve" viewBox="0 0 320 90" aria-hidden="true">
    <path d="M0 60 Q160 10 320 0 L320 90 L0 90 Z" fill="#0e5c4c"/>
    <path d="M0 52 Q160 2 320 -8" fill="none" stroke="#6cc070" stroke-width="4"/>
  </svg>
  <div class="front-wordmark"><span class="mark-square"></span>Timber Ridge<br>Land Services</div>

  <div class="person">
    <p class="person-name"><span class="first">Marta</span> <span class="last">Kovalen</span></p>
    <p class="person-role">Founder &amp; CEO</p>
  </div>

  <div class="divider divider-contact">
    <svg class="icon" viewBox="0 0 20 20" aria-label="Phone"><rect width="20" height="20" rx="5" fill="#6cc070"/><path d="M6 5l2 0 1 3-1.5 1a7 7 0 0 0 3.5 3.5L12 11l3 1v2a1 1 0 0 1-1 1A9 9 0 0 1 5 6a1 1 0 0 1 1-1z" fill="#fff"/></svg>
    <svg class="icon" viewBox="0 0 20 20" aria-label="Email"><rect width="20" height="20" rx="5" fill="#6cc070"/><rect x="4" y="6" width="12" height="8" fill="none" stroke="#fff" stroke-width="1.5"/><path d="M4 6l6 5 6-5" fill="none" stroke="#fff" stroke-width="1.5"/></svg>
    <svg class="icon" viewBox="0 0 20 20" aria-label="Website"><rect width="20" height="20" rx="5" fill="#6cc070"/><circle cx="10" cy="10" r="5.5" fill="none" stroke="#fff" stroke-width="1.5"/><path d="M4.5 10h11M10 4.5c-2.5 3-2.5 8 0 11M10 4.5c2.5 3 2.5 8 0 11" fill="none" stroke="#fff" stroke-width="1.2"/></svg>
  </div>

  <ul class="contact-list">
    <li>+001 555 210 4832</li>
    <li>info@timberridgeland.com</li>
    <li>www.timberridgeland.com</li>
  </ul>

  <div class="divider divider-address">
    <svg class="icon" viewBox="0 0 20 20" aria-label="Location"><rect width="20" height="20" rx="5" fill="#6cc070"/><path d="M10 4a4 4 0 0 1 4 4c0 3-4 8-4 8s-4-5-4-8a4 4 0 0 1 4-4z" fill="none" stroke="#fff" stroke-width="1.5"/><circle cx="10" cy="8" r="1.4" fill="#fff"/></svg>
  </div>

  <address class="address">1180 Cedar Mill Road •<br>Ashford, CO 80999</address>
</section>

</body>
</html>
```